Hospital Digital Whiteboard UI/UX Redesign

We are looking to update the look and feel of our Digital Whiteboards.
There are 4 separate layouts: Patient TV, Patient Room Whiteboard, Digital Door Sign, and Unit Care Board.
We want to have a unified, modern look across the portfolio.

```html
<!DOCTYPE html>
<html lang="en">
<head>
<meta charset="utf-8">
<title>Room 216 Door Sign</title>
<link rel="stylesheet" href="https://fonts.googleapis.com/css2?family=Montserrat:wght@500;600;700&display=swap">
<style>
  :root {
    --bg-top: #4a5cd0;
    --bg-mid: #2f62d6;
    --bg-bottom: #1a55cf;
    --pill-fill: #e0fdf8;
    --pill-edge: #ffffff;
    --accent-teal: #4ee6d6;
    --navy: #0b22a8;
    --button-navy: #031a9c;
    --button-edge: #3e5fd8;
    --text-light: #ffffff;
  }
  * { margin: 0; padding: 0; box-sizing: border-box; }
  html, body { width: 675px; height: 1200px; overflow: hidden; }
  body { font-family: "Montserrat", sans-serif; }

  .door-sign {
    position: relative;
    width: 675px;
    height: 1200px;
    overflow: hidden;
    background: linear-gradient(160deg, var(--bg-top) 0%, var(--bg-mid) 45%, var(--bg-bottom) 100%);
  }
  .backdrop-pattern {
    position: absolute; inset: 0;
    background: radial-gradient(ellipse at 70% 60%, rgba(90,110,230,0.25), rgba(0,0,0,0) 60%);
  }

  .room-badge {
    position: absolute;
    left: 128px; top: 154px;
    width: 419px; height: 198px;
    border-radius: 99px;
    background: var(--pill-edge);
    box-shadow: 0 8px 18px rgba(10,20,90,0.35);
  }
  .room-badge-inner {
    position: absolute; inset: 7px;
    border-radius: 92px;
    background: var(--pill-fill);
    border: 2px solid var(--accent-teal);
    color: var(--navy);
    text-align: center;
  }
  .room-label {
    position: absolute; left: 0; right: 0; top: 45px;
    font-size: 22px; font-weight: 600; letter-spacing: 0.5px;
  }
  .room-number {
    position: absolute; left: 0; right: 0; top: 72px;
    font-size: 64px; font-weight: 700; letter-spacing: -2px; line-height: 1;
  }

  .daily-quote {
    position: absolute;
    left: 80px; width: 515px; top: 472px;
    color: var(--text-light);
    text-align: center;
    font-size: 50px; font-weight: 600; line-height: 63px;
  }
  .quote-author {
    position: absolute;
    left: 0; right: 0; top: 716px;
    color: var(--text-light);
    text-align: center;
    font-size: 31px; font-weight: 500;
  }

  .facility-brand {
    position: absolute;
    left: 155px; top: 856px;
    width: 367px; height: 78px;
    background: #ffffff;
    border: 2px solid #c9d3f5;
    border-radius: 12px;
    display: flex; align-items: center; justify-content: center; gap: 10px;
  }
  .brand-dot { width: 16px; height: 16px; border-radius: 50%; background: var(--accent-teal); }
  .brand-name { font-size: 24px; font-weight: 600; color: var(--navy); }

  .action-button {
    position: absolute;
    top: 962px; height: 72px;
    background: var(--button-navy);
    border: 2px solid var(--button-edge);
    border-radius: 12px;
    display: flex; align-items: center;
    color: var(--text-light);
    font-size: 21px; font-weight: 600;
  }
  .action-admin { left: 154px; width: 162px; padding-left: 21px; gap: 13px; }
  .action-map { left: 332px; width: 190px; padding-left: 19px; gap: 13px; }
  .action-icon {
    width: 34px; height: 34px; border-radius: 50%;
    background: var(--accent-teal);
    display: flex; align-items: center; justify-content: center;
  }

  .device-code {
    position: absolute; right: 20px; top: 1163px;
    color: var(--text-light); font-size: 14px; font-family: Arial, sans-serif;
  }
</style>
</head>
<body>
<main class="door-sign">
  <div class="backdrop-pattern" role="img" aria-label="Faint pattern of medical cross outlines"></div>

  <section class="room-badge">
    <div class="room-badge-inner">
      <div class="room-label">ROOM</div>
      <div class="room-number">216</div>
    </div>
  </section>

  <p class="daily-quote">" Believe you can and you're halfway there."</p>
  <p class="quote-author">-Eleanor Whitfield</p>

  <div class="facility-brand">
    <span class="brand-dot"></span>
    <span class="brand-name">Clearwell Health</span>
  </div>

  <div class="action-button action-admin">
    <span class="action-icon">
      <svg width="14" height="17" viewBox="0 0 14 17" aria-hidden="true">
        <path d="M3.5 7V5a3.5 3.5 0 0 1 7 0v2" fill="none" stroke="#fff" stroke-width="2"/>
        <rect x="1" y="7" width="12" height="9" rx="1.5" fill="#fff"/>
        <rect x="6.2" y="9.5" width="1.6" height="3.5" fill="#4ee6d6"/>
      </svg>
    </span>
    <span>Admin</span>
  </div>

  <div class="action-button action-map">
    <span class="action-icon">
      <svg width="16" height="20" viewBox="0 0 16 20" aria-hidden="true">
        <path d="M8 1a7 7 0 0 0-7 7c0 5 7 11 7 11s7-6 7-11a7 7 0 0 0-7-7z" fill="#fff"/>
        <circle cx="8" cy="8" r="2.6" fill="#4ee6d6"/>
      </svg>
    </span>
    <span>Floor Map</span>
  </div>

  <span class="device-code">C50</span>
</main>
</body>
</html>
```